Modern Spot UV Business Card design

We are a relatively new real estate agency. We need a business card that reflects the professionalism and prestige of our company but is also modern and fresh, based around our logo.
We would love to utilise spot UV.
Happy to let the designers use their imagination and see what they come up with (we're not very creative, so have no ideas for you, sorry) :-)
We'd like one for each staff member, but I've just provided one staff members photo here to avoid confusion.

Target Market(s)

Families

Industry/Entity Type

Real Estate Agent

Contact Information for Business Card

Colin Varga - Director & Principal
Mobile: 0491 527 806
Email: colin.varga@vbrokers.example.com.au
Phone: (08) 7364 9150
Fax: (08) 7364 9182
www.vargabrokersrealestate.example.com.au

Font styles to use
Other font styles liked:
• Kabel Dm BT

Requirements
Must have
• Contact details, logo, photo, spot UV
Nice to have
• Modern interesting features that will make people comment. Nothing too feminine nor too masculine.
Should not have
• No houses! Nothing typical of a real estate agent.

```html
<!DOCTYPE html>
<html lang="en">
<head>
<meta charset="utf-8">
<title>Varga Brokers Real Estate – Business Card</title>
<link href="https://fonts.googleapis.com/css2?family=Montserrat:wght@400;500;600;800&display=swap" rel="stylesheet">
<style>
  :root {
    --stage: #2b2b2d;
    --card-black: #050505;
    --card-white: #ffffff;
    --ink: #1a1a1a;
    --ink-soft: #3a3a3a;
    --accent-blue: #1f9ad6;
    --accent-orange: #f29a1f;
    --photo-top: #3c3f44;
    --photo-bottom: #1b1c1f;
    --divider: #9a9a9a;
  }
  * { box-sizing: border-box; margin: 0; padding: 0; }
  html, body {
    width: 1200px; height: 900px; overflow: hidden;
    background: var(--stage);
    font-family: "Montserrat", Arial, sans-serif;
  }
  .canvas { position: relative; width: 1200px; height: 900px; }

  .card {
    position: absolute;
    width: 680px; height: 389px;
    border-radius: 26px;
    overflow: hidden;
    box-shadow: 0 18px 40px rgba(0,0,0,.45);
  }

  /* Shared brand lockup */
  .brand {
    display: flex; align-items: center; gap: 12px;
    font-weight: 800; line-height: 1.05; letter-spacing: -.5px;
    white-space: nowrap;
  }
  .brand__name span { display: block; }
  .brand__dot {
    flex: none; border-radius: 50%;
    background: var(--accent-orange);
  }
  .brand--light { color: #ffffff; font-size: 30px; }
  .brand--light .brand__dot { width: 30px; height: 30px; }
  .brand--dark { color: var(--ink); font-size: 24px; gap: 10px; }
  .brand--dark .brand__dot { width: 24px; height: 24px; }

  /* Front card */
  .card--front { left: 190px; top: 48px; background: var(--card-black); }
  .front__photo {
    position: absolute; right: 0; top: 0;
    width: 330px; height: 389px;
    background: radial-gradient(ellipse at 50% 35%, var(--photo-top), var(--photo-bottom) 70%, var(--card-black));
  }
  .front__brand { position: absolute; left: 48px; top: 190px; }
  .front__web {
    position: absolute; left: 48px; top: 312px;
    color: #ffffff; font-size: 14px; font-weight: 500;
  }
  .front__web .web-domain { color: var(--accent-orange); }

  /* Back card */
  .card--back { left: 330px; top: 470px; background: var(--card-white); }
  .back__brand { position: absolute; left: 36px; top: 168px; }
  .back__divider {
    position: absolute; left: 276px; top: 60px;
    width: 2px; height: 270px;
    background: linear-gradient(to bottom, transparent, var(--divider) 20%, var(--divider) 80%, transparent);
  }
  .contact { position: absolute; left: 296px; right: 18px; top: 86px; color: var(--ink); }
  .contact__name { color: var(--accent-blue); font-size: 30px; font-weight: 600; line-height: 1.1; }
  .contact__title { font-size: 15px; font-weight: 500; margin-bottom: 16px; color: var(--ink-soft); }
  .contact__list { list-style: none; }
  .contact__item {
    display: flex; align-items: center; gap: 9px;
    font-size: 13.5px; line-height: 24px; white-space: nowrap;
  }
  .contact__item svg { width: 13px; height: 13px; flex: none; fill: var(--accent-blue); }
  .contact__item .web-domain { color: var(--accent-blue); }
</style>
</head>
<body>
<main class="canvas">

  <section class="card card--front">
    <div class="front__photo" role="img" aria-label="Portrait photo of the agent in a grey suit on a black background"></div>
    <div class="front__brand">
      <div class="brand brand--light"><span class="brand__dot"></span><span class="brand__name"><span>Varga Brokers</span><span>Real Estate</span></span></div>
    </div>
    <p class="front__web">www.<span class="web-domain">vargabrokersrealestate.example.com.au</span></p>
  </section>

  <section class="card card--back">
    <div class="back__brand">
      <div class="brand brand--dark"><span class="brand__dot"></span><span class="brand__name"><span>Varga Brokers</span><span>Real Estate</span></span></div>
    </div>
    <div class="back__divider"></div>
    <div class="contact">
      <h1 class="contact__name">Colin Varga</h1>
      <p class="contact__title">Director &amp; Principal</p>
      <ul class="contact__list">
        <li class="contact__item">
          <svg viewBox="0 0 12 12" aria-hidden="true"><path d="M3 0h6a1 1 0 0 1 1 1v10a1 1 0 0 1-1 1H3a1 1 0 0 1-1-1V1a1 1 0 0 1 1-1zm0 1.5v8h6v-8z"/></svg>
          <span>0491 527 806</span>
        </li>
        <li class="contact__item">
          <svg viewBox="0 0 12 12" aria-hidden="true"><path d="M2.5 0.5l2 2.5-1.2 1.3c.8 1.7 2.1 3 3.7 3.7L8.3 6.8l2.7 2-1 2.4C4.8 11 1 7.2.3 2z"/></svg>
          <span>(08) 7364 9150</span>
        </li>
        <li class="contact__item">
          <svg viewBox="0 0 12 12" aria-hidden="true"><path d="M3 0h5v3H3zM1 4h10v6H9v2H3v-2H1zm3 4v3h4V8z"/></svg>
          <span>(08) 7364 9182</span>
        </li>
        <li class="contact__item">
          <svg viewBox="0 0 12 12" aria-hidden="true"><path d="M0 2h12v8H0zm1 1v.4l5 3.2 5-3.2V3z"/></svg>
          <span>colin.varga@vbrokers.example.com.au</span>
        </li>
        <li class="contact__item">
          <svg viewBox="0 0 12 12" aria-hidden="true"><path d="M6 0a6 6 0 1 0 0 12A6 6 0 0 0 6 0zm0 1c.8.9 1.3 2.4 1.4 4H4.6C4.7 3.4 5.2 1.9 6 1zM4.6 6h2.8c-.1 1.6-.6 3.1-1.4 4-.8-.9-1.3-2.4-1.4-4zM1 6h2.6c.1 1.5.5 2.8 1.1 3.8A5 5 0 0 1 1 6zm7.4 0H11a5 5 0 0 1-3.7 3.8c.6-1 1-2.3 1.1-3.8zM1 5a5 5 0 0 1 3.7-3.8C4.1 2.2 3.7 3.5 3.6 5zm7.4 0c-.1-1.5-.5-2.8-1.1-3.8A5 5 0 0 1 11 5z"/></svg>
          <span>www.<span class="web-domain">vargabrokersrealestate.example.com.au</span></span>
        </li>
      </ul>
    </div>
  </section>

</main>
</body>
</html>
```